Long Established Local Fencing (not swords) Business needs fresh Business Cards

We need fresh double sided business cards for our Fencing Construction business, we are looking for something with our new logo design added, and maybe a photo background ?
We recently had cards made from Cardlyne and we were horrified with what we got back, the quality was terrible, so am looking for high quality format for good printing company to make.
We install Steelmora, Timber paling, Aluminium Slat Screening, Picket (timber and aluminium) and most other fencing installations.
Our website is brankelrails.com.au should you like to learn a bit more.
We do have logo in other formats if required.
We have been in business for over 35 years and we have used this as a "motto" it is on our signage

Industry/Entity Type

Construction

Contact Information for Business Card

Open to ideas, we need 3 x different cards, one generic with no name and 2 x others each with 1 of our bosses name on each, I will put into upload files.

Colors
ec1f27
000000
606060
f5f5f5

Requirements
Must have
• Company Name and Logo
• Address
• Contact details, phone, website, email etc
• Small space to write notes when leaving card at residence
Nice to have
• Our motto "Building Coastal Boundaries for over three decades"

```html
<!DOCTYPE html>
<html lang="en">
<head>
<meta charset="utf-8">
<title>Brankel Rails – Business Cards</title>
<link href="https://fonts.googleapis.com/css2?family=Lato:ital,wght@0,400;0,700;0,900;1,400;1,700&display=swap" rel="stylesheet">
<style>
  :root{
    --red:#ec1f27;
    --black:#000000;
    --ink:#222222;
    --grey:#606060;
    --light:#f5f5f5;
    --backdrop:#e9e9e9;
    --white:#ffffff;
  }
  *{box-sizing:border-box;margin:0;padding:0}
  html,body{width:1200px;height:1117px;overflow:hidden}
  body{background:var(--backdrop);font-family:'Lato',sans-serif;position:relative}

  .card{position:absolute;left:210px;width:780px;height:476px;overflow:hidden;
        box-shadow:0 6px 18px rgba(0,0,0,.12)}
  .card--back{top:60px;background:#5a5a5a}
  .card--front{top:580px;background:var(--light)}

  /* back */
  .back-photo{position:absolute;inset:0;
    background:linear-gradient(160deg,#6d6e70 0%,#5e5f61 35%,#555657 70%,#4a4b4c 100%)}
  .back-content{position:absolute;inset:0;display:flex;flex-direction:column;
    align-items:center;justify-content:center;gap:26px;color:var(--white)}
  .brand{display:flex;align-items:center;gap:16px;font-weight:900;
    letter-spacing:3px;text-transform:uppercase}
  .brand__mark{width:30px;height:30px;background:var(--red)}
  .card--back .brand{font-size:52px;color:var(--white)}
  .motto{font-style:italic;font-size:24px;color:#e6e6e6}
  .motto strong{font-weight:700;color:var(--white)}

  /* front */
  .person{position:absolute;left:56px;top:52px}
  .person__name{font-weight:700;font-size:30px;color:var(--ink)}
  .person__role{font-size:22px;color:var(--red);margin-top:4px}
  .card--front .brand{position:absolute;right:56px;top:70px;font-size:36px;color:var(--black);gap:12px}
  .card--front .brand__mark{width:22px;height:22px}
  .address{position:absolute;right:56px;top:150px;text-align:right;font-size:20px;line-height:1.35;color:var(--ink)}
  .divider{position:absolute;left:56px;right:56px;top:222px;height:1px;background:#b5b5b5}
  .contacts{position:absolute;left:56px;top:246px;list-style:none;font-size:20px;color:var(--ink)}
  .contacts li{display:flex;align-items:center;gap:14px;height:32px}
  .contacts svg{width:16px;height:16px;flex:none}
  .stripe{position:absolute;left:0;bottom:0;width:100%;height:86px}
  .website{position:absolute;right:56px;bottom:13px;font-size:20px;color:var(--white);letter-spacing:.3px}
</style>
</head>
<body>

<section class="card card--back">
  <div class="back-photo" role="img" aria-label="Photo of a steel panel fence along a residential driveway, darkened with grey overlay"></div>
  <div class="back-content">
    <div class="brand"><span class="brand__mark"></span>Brankel Rails</div>
    <p class="motto">Building Coastal Boundaries for <strong>over three decades</strong></p>
  </div>
</section>

<section class="card card--front">
  <div class="person">
    <p class="person__name">Daniel Hartley</p>
    <p class="person__role">Managing Director</p>
  </div>

  <div class="brand"><span class="brand__mark"></span>Brankel Rails</div>

  <p class="address">42 Kestrel Avenue<br>Marlow Bay, Nsw 2391</p>

  <div class="divider"></div>

  <ul class="contacts">
    <li>
      <svg viewBox="0 0 16 16" aria-hidden="true"><path d="M4 1.5l2.2 3-1.3 1.6c.9 1.9 2.3 3.3 4.2 4.2l1.6-1.3 3 2.2-1.2 2.6C7.3 13.6 2.4 8.7 1.4 2.7z" fill="var(--red)"/></svg>
      02 4000 1287
    </li>
    <li>
      <svg viewBox="0 0 16 16" aria-hidden="true"><rect x="1" y="3" width="14" height="10" fill="none" stroke="var(--red)" stroke-width="1.5"/><path d="M1 3l7 6 7-6" fill="none" stroke="var(--red)" stroke-width="1.5"/></svg>
      office@brankelrails.com.au
    </li>
  </ul>

  <svg class="stripe" viewBox="0 0 780 86" preserveAspectRatio="none" aria-hidden="true">
    <polygon points="0,0 300,0 322,26 0,26" fill="var(--red)"/>
    <polygon points="0,30 325,30 340,46 780,46 780,86 0,86" fill="var(--grey)"/>
  </svg>
  <p class="website">www.brankelrails.com.au</p>
</section>

</body>
</html>
```